Consulting Group Website Landing Page Design

We are working with a Consulting Group in California. They provide consulting services to law enforcement agencies throughout the US.
Some sites to use for content:
https://www.marlowcrestcenter.org
https://www.jpellingroup.com
https://www.48rkventures.com
https://www.vdq.org
http://www.themirvalgroup.com
Thank you for taking the time to consider designing a website for us. We are web developers based in Stockton, CA, USA. Most of our projects go through the same process. Understanding this process may help you win a project with us. We custom-code all of our websites in-house. We don’t have any requirements as to what tools you use for your design, but we ask that you follow these guidelines. Plus, please send your designs in at least 1200px. wide so they do not pixelate when we show the client.
IMAGES:
If you use any images or icons in the design, we ask that you have a link to the asset so we can purchase the image/icon. Most of the designs we submit do not have the customer’s images on them unless they have some great images. Be creative; show us the feeling you are trying to portray with your image choices. Use any royalty-free site you choose. We subscribe to Velmora and mainly use their images, but we can purchase images outside of Velmora. PLEASE NOTE: we will not submit designs to clients with watermarks on the images.
FONTS:
We ask that you identify the fonts you’re using in the design. This can be done in a message if you want. We typically use Quintet Fonts and Velmora Fonts.
CONTENT:
We're always open to different content and ideas. We often submit designs with stock images so the client can see our vision. We typically take pictures after the website launch to use their images with our vision. Lorem Ipsum is fine for paragraphs, but we ask that you make the Headers with correct English. We want to be able to show the vision and identify the sections of the website.
INSPIRATION:
We typically add a couple of links in the brief of websites we like to help you get started in your design.
REVISIONS:
We do not often ask for revisions of the designs unless we see something in the design that may not appeal to the client. If there are slight changes that we want to make, we do that in the development process.
FEEDBACK:
We rarely give feedback on designs during the design process. We are working on many website projects and do not have the time to provide feedback. We usually respond if your request is well thought out and asks specific questions, but a note asking “feedback, please” usually goes unanswered.

```html
<!DOCTYPE html>
<html lang="en">
<head>
<meta charset="utf-8">
<title>Steelridge Consulting</title>
<link href="https://fonts.googleapis.com/css2?family=Poppins:wght@300;400;500;600;700&display=swap" rel="stylesheet">
<style>
:root{
  --navy:#1d479c;
  --navy-deep:#173a82;
  --purple:#2c2a78;
  --green:#6cb81f;
  --ink:#222;
  --muted:#555;
  --dark:#121212;
  --field:#2b2b2b;
  --white:#fff;
}
*{margin:0;padding:0;box-sizing:border-box}
html,body{width:1200px;height:5106px;overflow:hidden}
body{position:relative;font-family:'Poppins',sans-serif;color:var(--ink);background:var(--white)}
.abs{position:absolute}
.btn{position:absolute;display:flex;align-items:center;justify-content:space-between;padding:0 10px 0 18px;border-radius:24px;background:var(--purple);color:var(--white);font-size:13px;font-weight:500;border:2px solid var(--green);text-transform:uppercase}
.btn .dot{width:18px;height:18px;border-radius:50%;background:var(--white);display:flex;align-items:center;justify-content:center}
.btn .dot svg{width:10px;height:10px}
.section-title{position:absolute;font-size:40px;font-weight:400;color:var(--ink)}
.section-title b{font-weight:700}
.rule{position:absolute;width:74px;height:4px;background:var(--navy)}

/* header / hero */
.hero-photo{left:0;top:0;width:1200px;height:800px;background:linear-gradient(110deg,#2c3237 0%,#4d5357 40%,#262b30 70%,#1b1f24 100%)}
.hero-shape{left:0;top:0}
.brand{display:flex;align-items:center;gap:12px;color:var(--white);font-weight:600;font-size:30px}
.brand .mark{width:44px;height:44px;border-radius:50%;background:var(--navy);border:3px solid var(--white)}
.brand small{font-size:30px}
.socials{display:flex;gap:17px}
.socials span{width:37px;height:37px;border-radius:50%;border:2px solid var(--green);background:rgba(0,0,0,.2)}
.nav{left:600px;top:78px;display:flex;gap:46px;color:var(--white);font-size:16px;font-weight:500}
.nav .active{border-bottom:2px solid var(--green);padding-bottom:4px}
.hero-title{left:109px;top:262px;color:var(--white);font-size:56px;font-weight:700;line-height:70px;letter-spacing:-1px}
.slider-dots{left:108px;top:627px;display:flex;gap:10px}
.slider-dots i{width:13px;height:13px;border-radius:50%;border:2px solid var(--white)}
.slider-dots i.on{background:var(--green);border-color:var(--green)}
.scroll{left:1140px;top:332px;display:flex;flex-direction:column;align-items:center}
.scroll .ic{width:26px;height:26px;border-radius:50%;background:var(--green)}
.scroll .line{width:2px;height:160px;background:var(--white);margin-top:4px}
.scroll .label{position:absolute;top:120px;left:14px;transform:rotate(90deg);transform-origin:left top;color:var(--white);font-size:14px;white-space:nowrap}

/* about */
.about-circle{left:130px;top:912px;width:350px;height:350px;border-radius:50%;background:#e7ebf2}
.photo{position:absolute;border:2px solid var(--white);border-radius:4px}
.about-title{left:603px;top:894px;font-size:38px;font-weight:400}
.about-title b{font-weight:700}
.about-text{left:604px;top:976px;width:474px;font-size:14px;line-height:25px;color:#333;text-align:justify}
.about-text p+p{margin-top:8px}

/* services */
.card{position:absolute;width:310px;background:var(--white);border-radius:6px;padding:60px 16px 0 16px;box-shadow:0 6px 18px rgba(0,0,0,.15)}
.card svg{width:98px;height:98px;display:block}
.card h3{font-size:22px;font-weight:500;line-height:28px;margin-top:22px;color:var(--ink)}
.card p{font-size:13px;line-height:22.6px;color:#444;margin-top:12px}
.card.mid{border-bottom:6px solid var(--green)}

/* faq */
.faq{left:143px;width:911px}
.faq-row{position:absolute;left:0;width:911px;height:66px;border:1px solid #cfd5dd;border-radius:6px;background:var(--white);display:flex;align-items:center;padding-left:24px;font-size:20px;font-weight:600;color:var(--ink);box-shadow:0 3px 8px rgba(0,0,0,.06)}
.faq-row .toggle{position:absolute;right:-1px;top:-1px;width:68px;height:66px;background:var(--green);border-radius:0 6px 6px 0;display:flex;align-items:center;justify-content:center}
.faq-row .toggle i{width:30px;height:30px;border-radius:50%;background:var(--purple);color:var(--white);font-style:normal;font-size:22px;line-height:28px;text-align:center}
.faq-open{position:absolute;left:0;top:261px;width:911px;height:221px;border:1px solid #cfd5dd;border-radius:6px;box-shadow:0 4px 10px rgba(0,0,0,.08)}
.faq-open .head{height:66px;background:var(--green);border-radius:6px 6px 0 0;display:flex;align-items:center;padding-left:24px;color:var(--white);font-size:20px;font-weight:600;position:relative}
.faq-open .head i{position:absolute;right:19px;top:18px;width:30px;height:30px;border-radius:50%;background:var(--purple);color:var(--white);font-style:normal;text-align:center;line-height:28px;font-size:22px}
.faq-open p{padding:16px 24px 0 44px;font-size:16px;line-height:27px;color:#444}

/* how it works */
.how-title{left:0;width:1200px;top:3572px;text-align:center;font-size:40px;color:var(--navy)}
.how-title b{font-weight:700}
.how-sub{left:200px;width:800px;top:3670px;text-align:center;color:var(--white);font-size:28px;font-weight:600;line-height:36px}
.step{position:absolute;top:3785px;width:310px;border-left:3px solid var(--white);padding-left:20px;height:138px}
.step .num{position:absolute;left:20px;top:0;font-size:46px;font-weight:600;color:var(--white);line-height:56px}
.step h4{margin-left:48px;font-size:24px;font-weight:500;line-height:30px;color:var(--navy);text-transform:uppercase;padding-top:4px}
.step p{margin-top:14px;font-size:14px;line-height:26px;color:var(--white)}

/* contact */
.contact-text{left:145px;top:4292px;width:460px;font-size:16px;line-height:26px;color:#333}
.info{position:absolute;left:145px;display:flex;align-items:center;gap:22px}
.info .ic{width:36px;height:36px;border-radius:50%;background:var(--navy);display:flex;align-items:center;justify-content:center}
.info .ic svg{width:18px;height:18px}
.info small{display:block;font-size:12px;color:#555}
.info span{display:block;font-size:15px;font-weight:500;color:#222}
.field{position:absolute;left:629px;width:410px;height:41px;background:var(--field);border-radius:4px;color:#ddd;font-size:13px;padding:12px 18px}

/* footer */
.footer{left:0;top:4700px;width:1200px;height:340px;background:var(--dark)}
.footer-bar{left:0;top:5036px;width:1200px;height:70px;background:var(--green);color:#222;font-size:13px;text-align:center;line-height:70px}
.f-col{position:absolute;top:4786px;color:var(--white)}
.f-col h5{font-size:20px;font-weight:500}
.f-col .u{width:40px;height:3px;background:var(--green);margin:6px 0 12px}
.f-col li{list-style:none;font-size:13px;line-height:26px;color:#ddd}
.top-tab{left:1115px;top:5020px;width:40px;height:22px;background:var(--green);border-radius:6px 6px 0 0}
</style>
</head>
<body>

<!-- HERO -->
<div class="abs hero-photo" role="img" aria-label="Photograph of a uniformed security officer with arms crossed beside a metal gate"></div>
<svg class="abs hero-shape" width="1200" height="800" viewBox="0 0 1200 800">
  <polygon points="0,760 1200,790 1200,800 0,800" fill="#fff"/>
  <polygon points="0,665 600,778 0,770" fill="var(--green)"/>
</svg>
<div class="abs brand" style="left:112px;top:24px"><span class="mark"></span>Steelridge Consulting</div>
<div class="abs socials" style="left:785px;top:12px"><span></span><span></span><span></span></div>
<div class="btn" style="left:932px;top:8px;width:156px;height:42px;text-transform:uppercase">Contact Us<span class="dot"><svg viewBox="0 0 10 10"><path d="M3 2l4 3-4 3" stroke="#2c2a78" stroke-width="2" fill="none"/></svg></span></div>
<nav class="abs nav"><span class="active">Home</span><span>About</span><span>Services</span><span>Blog</span><span>Testimonials</span></nav>
<h1 class="abs hero-title">Protect and serve,<br>with honor</h1>
<div class="btn" style="left:109px;top:410px;width:146px;height:43px">Get Started<span class="dot"><svg viewBox="0 0 10 10"><path d="M3 2l4 3-4 3" stroke="#2c2a78" stroke-width="2" fill="none"/></svg></span></div>
<div class="abs slider-dots"><i></i><i class="on"></i><i></i></div>
<div class="abs scroll"><span class="ic"></span><span class="line"></span><span class="label">Scroll Down</span></div>

<!-- ABOUT -->
<div class="abs about-circle"></div>
<div class="photo" style="left:160px;top:914px;width:162px;height:183px;background:linear-gradient(160deg,#9aa26a,#4f5a40)" role="img" aria-label="Photograph of a police officer in a high-visibility vest"></div>
<div class="photo" style="left:95px;top:1114px;width:227px;height:160px;background:linear-gradient(160deg,#7c6a5c,#2f3340)" role="img" aria-label="Photograph of two police officers on a city street"></div>
<div class="photo" style="left:338px;top:914px;width:228px;height:335px;background:linear-gradient(170deg,#8a6d4d,#2b2f38)" role="img" aria-label="Photograph of a police officer in uniform with arms crossed"></div>
<h2 class="abs about-title">About <b>Steelridge Consulting</b></h2>
<div class="rule" style="left:604px;top:954px;width:22px"></div>
<div class="abs about-text">
  <p>Saerspiciatis undeasepoiise omnis isasdsesete natus error sit voluptatem accusan tisum doloremque laudantium, totam rem aperiam, ease aque ipaefdsa quae abse illo inventore veritatis et quasi architecto beatae vitae dicta sunt explicabo. Nemo enisdm ipsam voluptatem quiasea volupta sdease sessitasese aspernatur autodit sesaut fugitsdsed quia consequuntur magni dolores eos qui ratione voluptatem sequi nesciunt.</p>
  <p>Laaudantium, totam resadm aperiam, ease aqu ipaefdsa quae abse illo inventore veritatis ease quasi.</p>
</div>
<div class="btn" style="left:605px;top:1235px;width:146px;height:48px">Learn More<span class="dot"><svg viewBox="0 0 10 10"><path d="M3 2l4 3-4 3" stroke="#2c2a78" stroke-width="2" fill="none"/></svg></span></div>

<!-- SERVICES -->
<svg class="abs" style="left:0;top:1400px" width="1200" height="1110" viewBox="0 0 1200 1110">
  <defs><linearGradient id="svc" x1="0" y1="0" x2="1" y2="1"><stop offset="0" stop-color="#2456b0"/><stop offset="1" stop-color="#173a82"/></linearGradient></defs>
  <polygon points="0,45 1200,10 1200,930 0,1100" fill="url(#svc)"/>
  <polygon points="0,45 690,95 0,195" fill="var(--green)"/>
  <polygon points="690,1000 1200,925 1200,1010" fill="var(--green)"/>
</svg>
<div class="abs" style="left:0;top:1410px;width:1200px;height:1090px" role="img" aria-label="Faint background photograph of officers, tinted blue"></div>
<h2 class="section-title" style="left:0;width:1200px;text-align:center;top:1600px;color:#fff;font-weight:300">Our <b>Services</b></h2>
<div class="rule" style="left:563px;top:1666px;background:#fff"></div>

<div class="card" style="left:111px;top:1720px;height:468px">
  <svg viewBox="0 0 100 100" fill="none" stroke="#222" stroke-width="2.5"><circle cx="58" cy="60" r="12"/><circle cx="58" cy="60" r="24"/><path d="M58 30v-8M58 98v-8M28 60h-8M96 60h-8M37 39l-6-6M85 87l-6-6M79 39l6-6M31 87l6-6"/><circle cx="28" cy="28" r="9"/><circle cx="28" cy="28" r="16"/></svg>
  <h3>Systems<br>Assessment</h3>
  <p>Laerspiciatis unde omnis iste natus error sit voluptatem accusantium doloremque laudantium, totam rem aperiam, eaque ipsa quae ab illo inventore veritatis et quasi architecto beatae vitae dicta sunt explicabo. Nemo enim ipsam voluptatem quia voluptas sit aspernatur aut odit.</p>
</div>
<div class="card mid" style="left:444px;top:1805px;height:468px">
  <svg viewBox="0 0 100 100" fill="none" stroke="#222" stroke-width="2.5"><path d="M22 8h42l16 16v68H22z"/><path d="M64 8v16h16"/><path d="M32 40h36M32 50h36M32 60h36M32 70h24M32 80h30" stroke="#6cb81f"/></svg>
  <h3>Policy<br>Analysis</h3>
  <p>Laerspiciatis unde omnis iste natus error sit voluptatem accusantium doloremque laudantium, totam rem aperiam, eaque ipsa quae ab illo inventore veritatis et quasi architecto beatae vitae dicta sunt explicabo. Nemo enim ipsam voluptatem quia voluptas</p>
</div>
<div class="card" style="left:777px;top:1720px;height:468px">
  <svg viewBox="0 0 100 100" fill="none" stroke="#222" stroke-width="2.5"><rect x="8" y="10" width="66" height="80"/><rect x="16" y="20" width="18" height="20"/><path d="M42 24h24M42 34h24M16 52h30M16 62h24M16 72h20" stroke="#6cb81f"/><circle cx="66" cy="64" r="14"/><path d="M76 74l14 14"/></svg>
  <h3>Independent<br>Investigations</h3>
  <p>Laerspiciatis unde omnis iste natus error sit voluptatem accusantium doloremque laudantium, totam rem aperiam, eaque ipsa quae ab illo inventore veritatis et quasi architecto beatae vitae dicta sunt explicabo. Nemo enim ipsam voluptatem quia voluptas sit aspernatur aut odit.</p>
</div>

<!-- FAQ -->
<h2 class="section-title" style="left:0;width:1200px;text-align:center;top:2574px">Frequently Asked <b>Question</b></h2>
<div class="abs faq" style="top:2707px;height:482px">
  <div class="faq-row" style="top:0">Kaerspiciatis unde omnis iste natus error sit voluptatem<span class="toggle"><i>+</i></span></div>
  <div class="faq-row" style="top:89px">Eaventore veritatis et quasi architecto beatae vitae dicta sunt explicabo<span class="toggle"><i>+</i></span></div>
  <div class="faq-row" style="top:174px">Hauia consequuntur magni dolores eos qui ratione voluptatem<span class="toggle"><i>+</i></span></div>
  <div class="faq-open">
    <div class="head">Gatem vel eum iure reprehenderit qui in ea voluptate<i>&minus;</i></div>
    <p>Ioerspiciatis unde omnis iste natus error sit voluptatem accusantium doloremque laudantium, totam rem aperiam, eaque ipsa quae ab illo inventore veritatis et quasi architecto beatae vitae dicta sunt explicabo. Nemo enim ipsam voluptatem quia voluptas sit aspernatur aut</p>
  </div>
</div>
<div class="btn" style="left:527px;top:3226px;width:146px;height:46px">Learn More<span class="dot"><svg viewBox="0 0 10 10"><path d="M3 2l4 3-4 3" stroke="#2c2a78" stroke-width="2" fill="none"/></svg></span></div>

<!-- HOW IT WORKS -->
<svg class="abs" style="left:0;top:3310px" width="1200" height="840" viewBox="0 0 1200 840">
  <polygon points="0,6 1200,100 1200,720 0,720" fill="var(--green)"/>
  <polygon points="520,100 1200,40 1200,190" fill="var(--navy)"/>
  <polygon points="0,715 1200,720 1200,830 0,830" fill="var(--green)"/>
  <polygon points="0,715 1200,820 1200,830 0,830" fill="#fff"/>
  <polygon points="0,715 1200,800 0,770" fill="var(--navy)"/>
</svg>
<h2 class="abs how-title" style="font-weight:400">How It <b>Works</b></h2>
<div class="rule" style="left:563px;top:3643px"></div>
<p class="abs how-sub">Haerspiciatis unde omnis iste natus error sit voluptatem accusantium doloremque laudantium.</p>
<div class="step" style="left:109px"><span class="num">1.</span><h4>Omnisiste natus error</h4><p>Haerspiciatis unde omnis iste natus error sit voluptatem accusantium doloremque laudantium, totam rem.</p></div>
<div class="step" style="left:440px"><span class="num">2.</span><h4>Accusantium doloremque</h4><p>Haerspiciatis unde omnis iste natus error sit voluptatem accusantium doloremque laudantium, totam rem.</p></div>
<div class="step" style="left:775px"><span class="num">3.</span><h4>Architecto beatae vitae</h4><p>Haerspiciatis unde omnis iste natus error sit voluptatem accusantium doloremque laudantium, totam rem.</p></div>

<!-- CONTACT -->
<h2 class="section-title" style="left:145px;top:4200px">Contact <b>Us</b></h2>
<p class="abs contact-text">Perspiciatis unde omnis iste natus error ssadsdit voluptatem accusantium doloremque laudantium, totam rem aperiam, eaque ipsa quaasde abasel isdllo inventore veritatis et quasi architecto beatsdae vitae dicta sunt explicabo. Nemo enim ipsam voluptatemfugit.</p>
<div class="info" style="top:4424px"><span class="ic"><svg viewBox="0 0 24 24"><path d="M6 3l4 4-2 3c1 3 3 5 6 6l3-2 4 4-3 3C10 21 3 14 3 6z" fill="#fff"/></svg></span><div><small>Call Us</small><span>0421 586 903</span></div></div>
<div class="info" style="top:4488px"><span class="ic"><svg viewBox="0 0 24 24"><rect x="3" y="6" width="18" height="12" fill="#fff"/><path d="M3 6l9 7 9-7" stroke="#1d479c" stroke-width="2" fill="none"/></svg></span><div><small>Email</small><span>info@steelridgeconsulting.com</span></div></div>
<div class="info" style="top:4550px"><span class="ic"><svg viewBox="0 0 24 24"><path d="M12 2a7 7 0 017 7c0 5-7 13-7 13S5 14 5 9a7 7 0 017-7z" fill="#fff"/><circle cx="12" cy="9" r="2.5" fill="#1d479c"/></svg></span><div><small>Address</small><span>1482 Harlow Street, Los Angeles, CA 90017</span></div></div>

<div class="field" style="top:4250px">Your Name</div>
<div class="field" style="top:4309px">Email</div>
<div class="field" style="top:4369px">Phone Number</div>
<div class="field" style="top:4428px;height:125px">Enter Your Message</div>
<div class="btn" style="left:629px;top:4575px;width:144px;height:44px">Submit<span class="dot"><svg viewBox="0 0 10 10"><path d="M3 2l4 3-4 3" stroke="#2c2a78" stroke-width="2" fill="none"/></svg></span></div>

<!-- FOOTER -->
<div class="abs footer"></div>
<div class="abs brand" style="left:169px;top:4800px"><span class="mark"></span>Steelridge Consulting</div>
<div class="abs socials" style="left:246px;top:4906px"><span></span><span></span><span></span></div>
<div class="f-col" style="left:539px"><h5>Quick Links</h5><div class="u"></div><ul><li>Home</li><li>About</li><li>Services</li><li>Blog</li><li>Testimonials</li><li>Contact Us</li></ul></div>
<div class="f-col" style="left:752px"><h5>Links</h5><div class="u"></div><ul><li>Copyright</li><li>Legal</li><li>Privacy</li><li>Accessibility</li><li>Sitemap</li></ul></div>
<div class="f-col" style="left:928px"><h5>Support</h5><div class="u"></div><ul><li>Team</li><li>About Us</li><li>Careers</li><li>Our Values</li></ul></div>
<div class="abs footer-bar">&copy;2023. All rights reserved.</div>
<div class="abs top-tab"></div>

</body>
</html>
```